LOCAL TAXI SERVICE NEEDS A BANNER AD DESIGN

NEED BANNER AD DESIGN FOR TAXI SERVICE IN NJ. WE PROVIDE LOCAL AND LONG DISTANCE TRANSPORTATION. OUR MAIN BASE OF CUSTOMER GO TO THE MAJOR AIRPORTS IN THE TRI STATE AREA. I WANT TO OFFER A SPECIAL GOING TO DALMORE AIRPORT OF $35.00 WITH A COUPON CODE OF CP 12. THIS BANNER AD WILL BE USED FOR MY CHIRPLANE PAGE

Target Market(s)

PEOPLE WHO TRAVEL A LOT

Industry/Entity Type

Taxi

Font styles to use
Serif
Sans Serif

Colors
0792cd
0255a3
33a6d7
85cae6
cee9f5
ecf7fb
ffffff

Requirements
Must have
• MY COMPANY NAME: MAVIN'S TAXI

```html
<!DOCTYPE html>
<html lang="en">
<head>
<meta charset="utf-8">
<title>Mavin's Taxi cover banner</title>
<link rel="stylesheet" href="https://fonts.googleapis.com/css2?family=Anton&family=Open+Sans:wght@400;600&family=Passion+One:wght@700&family=Roboto+Slab:wght@700&display=swap">
<style>
  :root {
    --deep-blue: #0255a3;
    --ocean-blue: #0792cd;
    --sky-blue: #33a6d7;
    --pale-blue: #85cae6;
    --mist-blue: #cee9f5;
    --ice-blue: #ecf7fb;
    --white: #ffffff;
    --ink-blue: #0a2f6b;
    --page-bg: #e9edf3;
  }
  html, body {
    margin: 0;
    width: 1200px;
    height: 921px;
    overflow: hidden;
    background: var(--page-bg);
  }
  .stage {
    position: relative;
    width: 1200px;
    height: 921px;
  }
  .cover-banner {
    position: absolute;
    left: 40px;
    top: 253px;
    width: 927px;
    height: 343px;
    transform: scale(1.2082);
    transform-origin: 0 0;
    overflow: hidden;
    background: linear-gradient(180deg, var(--deep-blue) 0%, var(--ocean-blue) 45%, var(--sky-blue) 80%, var(--pale-blue) 100%);
    font-family: "Open Sans", sans-serif;
  }
  .city-backdrop {
    position: absolute;
    left: 0; top: 0;
    width: 927px; height: 311px;
    background: radial-gradient(ellipse at 60% 80%, rgba(133,202,230,0.45), rgba(133,202,230,0) 65%);
  }
  .brand-name {
    position: absolute;
    left: 16px; top: 8px;
    display: flex; align-items: center; gap: 8px;
    color: var(--white);
    font-family: "Open Sans", sans-serif;
    font-weight: 400;
    font-size: 24px;
    letter-spacing: 0.5px;
  }
  .brand-name .brand-square {
    width: 22px; height: 22px;
    background: var(--white);
  }
  .headline {
    position: absolute;
    left: 362px; top: 2px;
    width: 522px;
    margin: 0;
    text-align: center;
    font-family: "Passion One", sans-serif;
    font-weight: 700;
    font-size: 37px;
    line-height: 40px;
    color: #4fd2f5;
    -webkit-text-stroke: 1px var(--white);
  }
  .promo-box {
    position: absolute;
    left: 13px; top: 86px;
    width: 285px; height: 76px;
    border: 1px solid var(--mist-blue);
    color: var(--white);
    text-align: center;
  }
  .promo-offer {
    margin: 2px 0 0;
    font-family: "Anton", sans-serif;
    letter-spacing: 0.5px;
    white-space: nowrap;
  }
  .promo-offer .amount { font-size: 36px; }
  .promo-offer .detail { font-size: 16px; }
  .promo-code {
    margin: -2px 0 0;
    font-size: 17px;
    letter-spacing: 1.5px;
  }
  .route {
    position: absolute;
    top: 54px;
    width: 150px;
    margin-left: -75px;
    text-align: center;
  }
  .route-label {
    margin: 0;
    font-family: "Roboto Slab", serif;
    font-weight: 700;
    font-size: 22px;
    line-height: 20px;
    letter-spacing: 1px;
    color: var(--white);
    -webkit-text-stroke: 0.8px var(--ink-blue);
  }
  .route-pole {
    width: 3px; height: 12px;
    margin: 2px auto 0;
    background: var(--white);
  }
  .route-photo {
    position: absolute;
    top: 116px;
    width: 140px; height: 140px;
    margin-left: -73px;
    border-radius: 50%;
    border: 3px solid var(--white);
  }
  .photo-white-sedan { background: radial-gradient(circle at 45% 60%, #f4f4f2, #9ea7a9 70%, #5e6b5a); }
  .photo-black-suv { background: radial-gradient(circle at 50% 60%, #3a3a3c, #141416 70%, #6f6048); }
  .photo-green-sedan { background: radial-gradient(circle at 50% 60%, #d6ee86, #a9c84f 60%, #8a8f86); }
  .photo-yellow-cab { background: radial-gradient(circle at 50% 55%, #f4c430, #e0a415 60%, #5a5650); }
  .route-price {
    position: absolute;
    top: 264px;
    width: 120px;
    margin-left: -60px;
    margin-top: 0;
    text-align: center;
    font-family: "Anton", sans-serif;
    font-size: 29px;
    line-height: 34px;
    color: var(--white);
    -webkit-text-stroke: 1px var(--deep-blue);
  }
  .base-rule {
    position: absolute;
    left: 0; top: 309px;
    width: 927px; height: 5px;
    background: var(--white);
  }
  .base-band {
    position: absolute;
    left: 0; top: 314px;
    width: 927px; height: 29px;
    background: linear-gradient(90deg, var(--pale-blue), var(--mist-blue) 50%, var(--pale-blue));
  }
</style>
</head>
<body>
<main class="stage">
  <section class="cover-banner" aria-label="Mavin's Taxi Chirplane cover banner">
    <div class="city-backdrop" role="img" aria-label="Faint blue city skyline behind the banner"></div>

    <div class="brand-name"><span class="brand-square"></span>MAVIN'S TAXI</div>

    <h1 class="headline">Mavin's Taxis Are At Your Service</h1>

    <div class="promo-box">
      <p class="promo-offer"><span class="amount">$35</span> <span class="detail">off to DALMORE Airport</span></p>
      <p class="promo-code">USE PROMOCODE CP12</p>
    </div>

    <div class="route" style="left:421px"><p class="route-label">To Dalmore<br>Airport</p><div class="route-pole"></div></div>
    <div class="route" style="left:554px"><p class="route-label">To ELM<br>Airport</p><div class="route-pole"></div></div>
    <div class="route" style="left:692px"><p class="route-label">To KRV<br>Airport</p><div class="route-pole"></div></div>
    <div class="route" style="left:834px"><p class="route-label">To PWT<br>Airport</p><div class="route-pole"></div></div>

    <div class="route-photo photo-white-sedan" style="left:421px" role="img" aria-label="Photo of a white sedan taxi"></div>
    <div class="route-photo photo-black-suv" style="left:554px" role="img" aria-label="Photo of a black luxury SUV"></div>
    <div class="route-photo photo-green-sedan" style="left:692px" role="img" aria-label="Photo of a lime green sedan"></div>
    <div class="route-photo photo-yellow-cab" style="left:834px" role="img" aria-label="Photo of a yellow taxi cab"></div>

    <p class="route-price" style="left:421px">$40</p>
    <p class="route-price" style="left:554px">$125</p>
    <p class="route-price" style="left:692px">$140</p>
    <p class="route-price" style="left:834px">$190</p>

    <div class="base-rule"></div>
    <div class="base-band"></div>
  </section>
</main>
</body>
</html>
```